Creative Challenge - Disruptive Digital Construction Business needs an Application Design

We need an application design (4 screens).
The app will offer easy-to-use an interactive course to illustrate the latest technology to construction professionals. Kindly find the attachments.
Updates

I have just posted the contest and the deadline is tomorrow!! Please give me my original 7 days back.

Need extra days to review

Target Market(s)

Construction professionals, aged from 22 to 36, who want to learn new disruptive technologies in construction.

Colors
e667a6
b868aa
33a6d7

Requirements
Must have
• The name of the app, Velmiro, stands for “Virtual Engineering Leaders”. The user is a Velmiro, who would transform the digital construction industry. We want a design that gives that feel to the users.

```html
<!DOCTYPE html>
<html lang="en">
<head>
<meta charset="utf-8">
<title>Learning App Screens</title>
<link rel="stylesheet" href="https://fonts.googleapis.com/css2?family=Quicksand:wght@400;500;600;700&display=swap">
<style>
  :root{
    --page:#f6e9f0;
    --screen:#f3f2f5;
    --ink:#1f1f2b;
    --muted:#4a4a57;
    --pink:#e667a6;
    --purple:#b868aa;
    --blue:#33a6d7;
    --pink-soft:#f6dde9;
    --blue-soft:#e6f0f6;
    --line:#d8d6dc;
    --green:#4fa35a;
    --olive:#a8a23c;
    --teal:#3b9aa0;
    --red:#c8504f;
    --violet:#8a4fc2;
  }
  *{box-sizing:border-box;margin:0;padding:0}
  html,body{width:1200px;height:900px;overflow:hidden}
  body{background:var(--page);font-family:"Quicksand",sans-serif;color:var(--ink);position:relative}
  .screen{position:absolute;width:196px;height:408px;background:var(--screen);border-radius:22px;overflow:hidden;box-shadow:0 6px 22px rgba(120,80,110,.15)}
  .status{position:absolute;top:10px;left:18px;right:18px;display:flex;justify-content:space-between;font-size:7px;font-weight:600}
  .status .bars{display:flex;gap:3px;align-items:center}
  .status .bars i{display:block;width:10px;height:5px;background:var(--ink);border-radius:1px}
  .abs{position:absolute}
  .art{position:absolute;border-radius:50%}
  .center{text-align:center;left:0;right:0}
  .btn{position:absolute;height:21px;border-radius:2px;font-size:7.5px;display:flex;align-items:center;justify-content:center;font-weight:500}
  .btn.solid{background:var(--blue);color:#fff}
  .btn.ghost{border:1px solid var(--blue);color:var(--blue);background:transparent}
  .tabbar{position:absolute;left:0;right:0;bottom:0;height:40px;border-top:1px solid #e3e1e6;display:flex;justify-content:space-around;align-items:center;padding-bottom:4px}
  .tab{display:flex;flex-direction:column;align-items:center;font-size:4px;color:var(--muted);gap:1px}
  .tab svg{width:11px;height:11px}
  .field-label{position:absolute;left:18px;font-size:7px;color:var(--muted)}
  .field{position:absolute;left:18px;right:18px;height:16px;border-bottom:1.5px solid var(--blue);font-size:7px;display:flex;justify-content:space-between;align-items:center}
  .social{position:absolute;width:20px;height:20px;border:1px solid var(--ink);border-radius:50%;display:flex;align-items:center;justify-content:center;font-size:4px;font-weight:600}
  .module{position:absolute;width:80px;height:68px;background:#f6f5f7;border-radius:2px;box-shadow:0 1px 3px rgba(0,0,0,.07);border-bottom:2px solid}
  .module .num{position:absolute;left:11px;top:16px;font-size:7px;font-weight:600}
  .module .blob{position:absolute;left:-6px;top:-6px;width:42px;height:42px;border-radius:50%;opacity:.35}
  .module .name{position:absolute;left:5px;bottom:8px;font-size:7px;line-height:1.2}
  .step{position:absolute;left:30px;right:10px;font-size:6.5px;line-height:1.35}
  .step::before{content:"";position:absolute;left:-8px;top:2px;width:4px;height:4px;border-radius:50%;background:var(--pink)}
  .attach{position:absolute;left:8px;right:14px;height:20px;background:#f8f7f9;box-shadow:0 1px 3px rgba(0,0,0,.07);display:flex;align-items:center;padding:0 8px;gap:7px;font-size:7px}
  .attach .doc{width:5px;height:7px;background:var(--pink);border-radius:1px}
  .attach .dl{margin-left:auto;color:var(--blue);font-size:8px}
</style>
</head>
<body>

<!-- Onboarding -->
<section class="screen" style="left:58px;top:30px">
  <div class="status"><span>9:41</span><span class="bars"><i></i></span></div>
  <div class="art" role="img" aria-label="Illustration of a professional leaning on a stack of books beside a construction crane" style="left:30px;top:70px;width:136px;height:130px;border-radius:40% 40% 30% 30%;background:linear-gradient(160deg,#e6e2ea,#c962a3 70%,#7a2f6a)"></div>
  <div class="abs center" style="top:242px;font-size:10.5px;font-weight:700;line-height:1.25">Lorem dolor sit amet<br>consectetur adipisicing elit</div>
  <div class="abs center" style="top:285px;font-size:6px;line-height:1.35;color:var(--muted)">Lorem dolor sit amet consectetur adipisicing eli<br>sed do eiusmod tempor</div>
  <div class="abs center" style="top:330px;display:flex;justify-content:center;gap:6px;align-items:center">
    <i style="width:4px;height:4px;border-radius:50%;background:var(--ink)"></i><i style="width:6px;height:6px;border-radius:50%;background:var(--ink)"></i><i style="width:4px;height:4px;border-radius:50%;background:var(--ink)"></i><i style="width:4px;height:4px;border-radius:50%;background:var(--ink)"></i>
  </div>
  <div class="abs" style="right:20px;top:360px;font-size:6.5px;color:var(--muted)">SKIP</div>
</section>

<!-- Welcome -->
<section class="screen" style="left:365px;top:30px">
  <div class="status"><span>9:41</span><span class="bars"><i></i></span></div>
  <div class="art" role="img" aria-label="Illustration of a professional in an egg chair working on a laptop" style="left:38px;top:58px;width:118px;height:140px;border-radius:48% 48% 30% 30%;background:linear-gradient(160deg,#dcd9e2,#8f8ba0 55%,#b23d83)"></div>
  <div class="abs center" style="top:232px;font-size:17px;font-weight:500">Welcome</div>
  <div class="abs center" style="top:262px;font-size:6.2px;line-height:1.45;color:var(--muted)">Please login or sign up to continue<br>using this app</div>
  <div class="btn solid" style="left:28px;top:305px;width:65px">Login</div>
  <div class="btn ghost" style="left:106px;top:305px;width:65px">Signup</div>
</section>

<!-- Login -->
<section class="screen" style="left:664px;top:30px">
  <div class="status"><span>9:41</span><span class="bars"><i></i></span></div>
  <div class="abs" style="left:18px;top:75px;font-size:17px;font-weight:500">Name here</div>
  <div class="abs" style="left:18px;top:103px;font-size:10px;font-weight:500;color:var(--muted)">Welcome back!</div>
  <div class="field-label" style="top:142px">Email</div>
  <div class="field" style="top:153px"><span>username@mail.com</span>
    <svg width="8" height="8" viewBox="0 0 10 10"><circle cx="5" cy="3" r="2.2" fill="#1f1f2b"/><path d="M1 10c0-3 2-4.5 4-4.5S9 7 9 10z" fill="#1f1f2b"/></svg></div>
  <div class="field-label" style="top:180px">Password</div>
  <div class="field" style="top:191px"><span style="letter-spacing:1px">**********</span>
    <svg width="11" height="7" viewBox="0 0 12 8"><path d="M0 4C2 0 10 0 12 4 10 8 2 8 0 4z" fill="#1f1f2b"/><circle cx="6" cy="4" r="1.7" fill="#f3f2f5"/></svg></div>
  <div class="abs" style="right:18px;top:213px;font-size:5.8px;color:var(--blue)">Forgot Password?</div>
  <div class="btn solid" style="left:18px;right:18px;top:238px">Login</div>
  <div class="abs" style="left:18px;right:18px;top:285px;display:flex;align-items:center;gap:5px;font-size:6px;color:var(--muted)">
    <i style="flex:1;height:1px;background:var(--line)"></i>Or Signup With<i style="flex:1;height:1px;background:var(--line)"></i></div>
  <div class="social" style="left:40px;top:310px">Linkora</div>
  <div class="social" style="left:89px;top:310px">Chirpo</div>
  <div class="social" style="left:138px;top:310px">Searvo</div>
  <div class="abs center" style="top:348px;font-size:6px;color:var(--muted)">New Member? <span style="color:var(--blue)">Sign up</span></div>
</section>

<!-- Home -->
<section class="screen" style="left:956px;top:30px">
  <div class="status"><span>9:41</span><span class="bars"><i></i></span></div>
  <div class="abs" style="left:18px;top:30px;font-size:8.5px;font-weight:700">Hello User!</div>
  <div class="art" role="img" aria-label="Illustration of a professional sitting on a large book" style="left:58px;top:50px;width:78px;height:86px;border-radius:46% 46% 30% 30%;background:linear-gradient(160deg,#e0dde6,#7f3b78 60%,#c45699)"></div>
  <div class="abs" style="left:14px;right:14px;top:150px;height:26px;background:var(--blue-soft);display:flex;align-items:center;gap:10px;padding:0 6px;font-size:6px;color:var(--muted)">
    <span style="background:var(--blue);color:#fff;font-size:8px;padding:4px 8px">New</span>Explore 6 more resources<span style="margin-left:auto">⌄</span></div>
  <div class="abs" style="left:18px;top:195px;font-size:8.5px;font-weight:700">Continue Reading</div>
  <div class="abs" style="left:14px;right:14px;top:212px;height:64px;background:var(--pink-soft);padding:8px 6px">
    <div style="font-size:8.5px;font-weight:500;border-left:1px solid var(--pink);padding-left:3px">BIM Project Management</div>
    <div style="font-size:5.8px;margin-top:11px">02</div>
    <div style="font-size:5.8px;display:flex;justify-content:space-between;margin-top:2px"><span>Invitation to Tender</span><span>Progress: 10%</span></div>
    <div style="height:1.5px;background:#f0bcd5;margin-top:6px"><div style="width:10%;height:100%;background:var(--pink)"></div></div>
  </div>
  <div class="art" role="img" aria-label="Illustration of a professional beside a mobile phone" style="left:26px;top:300px;width:34px;height:38px;border-radius:4px;background:linear-gradient(160deg,#c9dbe8,#2e3a5c)"></div>
  <div class="abs" style="left:78px;top:303px;font-size:5.5px;line-height:1.4">Learn new disruptive<br>technology in construction.</div>
  <div class="abs" style="left:78px;top:327px;border:1px solid var(--blue);color:var(--blue);font-size:4.5px;padding:3px 9px">Explore more</div>
  <nav class="tabbar">
    <span class="tab" style="color:var(--ink)"><svg viewBox="0 0 12 12"><path d="M6 1 1 6h1.5v5h3V8h1v3h3V6H11z" fill="#1f1f2b"/></svg>Home</span>
    <span class="tab"><svg viewBox="0 0 12 12"><rect x="3" y="1" width="6" height="10" fill="none" stroke="#555"/></svg>Resources</span>
    <span class="tab"><svg viewBox="0 0 12 12"><path d="M1 3l3-1 4 1 3-1v7l-3 1-4-1-3 1z" fill="none" stroke="#555"/></svg>Activites</span>
    <span class="tab"><svg viewBox="0 0 12 12"><circle cx="6" cy="4" r="2.3" fill="none" stroke="#555"/><path d="M2 11c0-3 2-4 4-4s4 1 4 4z" fill="none" stroke="#555"/></svg>Profile</span>
  </nav>
</section>

<!-- Modules -->
<section class="screen" style="left:148px;top:468px;height:408px">
  <div class="status"><span>9:41</span><span class="bars"><i></i></span></div>
  <div class="abs" style="left:12px;top:26px;font-size:8.5px;font-weight:600">Modules</div>
  <div class="module" style="left:12px;top:41px;border-color:var(--pink)"><i class="blob" style="background:#ecd5df"></i><span class="num">01</span><span class="name">Assessment &amp; Needs</span></div>
  <div class="module" style="left:100px;top:41px;border-color:var(--blue)"><i class="blob" style="background:#d6e4ee"></i><span class="num">02</span><span class="name">Invitation to Tender</span></div>
  <div class="module" style="left:12px;top:117px;border-color:var(--purple)"><i class="blob" style="background:#e7d6e5"></i><span class="num">03</span><span class="name">Tender Response</span></div>
  <div class="module" style="left:100px;top:117px;border-color:var(--teal)"><i class="blob" style="background:#d5e8ea"></i><span class="num">04</span><span class="name">Appointment</span></div>
  <div class="module" style="left:12px;top:193px;border-color:var(--green)"><i class="blob" style="background:#dcebdc"></i><span class="num">05</span><span class="name">Mobilization</span></div>
  <div class="module" style="left:100px;top:193px;border-color:var(--olive)"><i class="blob" style="background:#ecebd3"></i><span class="num">06</span><span class="name">Collaborative Prod.<br>of Information</span></div>
  <div class="module" style="left:12px;top:269px;border-color:var(--red)"><i class="blob" style="background:#efdcdc"></i><span class="num">07</span><span class="name">Information Model<br>Delivery</span></div>
  <div class="module" style="left:100px;top:269px;border-color:var(--violet)"><i class="blob" style="background:#e6dcef"></i><span class="num">08</span><span class="name">Project close-out</span></div>
  <nav class="tabbar">
    <span class="tab" style="color:var(--ink)"><svg viewBox="0 0 12 12"><path d="M6 1 1 6h1.5v5h3V8h1v3h3V6H11z" fill="#1f1f2b"/></svg>Home</span>
    <span class="tab"><svg viewBox="0 0 12 12"><rect x="3" y="1" width="6" height="10" fill="none" stroke="#555"/></svg>Resources</span>
    <span class="tab"><svg viewBox="0 0 12 12"><path d="M1 3l3-1 4 1 3-1v7l-3 1-4-1-3 1z" fill="none" stroke="#555"/></svg>Activites</span>
    <span class="tab"><svg viewBox="0 0 12 12"><circle cx="6" cy="4" r="2.3" fill="none" stroke="#555"/><path d="M2 11c0-3 2-4 4-4s4 1 4 4z" fill="none" stroke="#555"/></svg>Profile</span>
  </nav>
</section>

<!-- Module detail -->
<section class="screen" style="left:508px;top:464px;height:408px">
  <div class="abs" style="left:0;right:0;top:0;height:130px;background:var(--pink-soft)"></div>
  <div class="status"><span>9:41</span><span class="bars"><i></i></span></div>
  <div class="abs" style="left:8px;top:20px;width:10px;height:10px;border-radius:50%;background:#7a7a84;color:#fff;font-size:7px;line-height:10px;text-align:center">‹</div>
  <div class="abs" style="left:22px;top:34px;font-size:8px;font-weight:600">01</div>
  <div class="abs" style="left:22px;top:46px;font-size:9px;font-weight:700">Assessment &amp; Needs</div>
  <div class="abs" style="left:22px;right:12px;top:64px;font-size:7px;line-height:1.3;color:var(--muted)">Lorem ipsum dolor sit amet, consetetur sadipscing elitr, sed diam nonumy eirmod tempor invidunt ut labore et dolore magna aliquyam erat, sed diam voluptua. At vero eos et accusam et justo duo.</div>
  <div class="abs" style="left:24px;top:146px;bottom:0;border-left:1px dashed #c9c6cc"></div>
  <div class="step" style="top:141px">Appoint Individuals to undertake the information management function</div>
  <div class="abs" style="left:45px;top:163px;font-size:5.8px">Progress: 10%</div>
  <div class="abs" style="left:41px;width:108px;top:175px;height:2px;background:#f0bcd5"><div style="width:12%;height:100%;background:var(--pink)"></div></div>
  <div class="btn solid" style="left:43px;top:188px;width:42px;height:13px;font-size:6px">Explore</div>
  <div class="btn ghost" style="left:98px;top:188px;width:50px;height:13px;font-size:6px">Download</div>
  <div class="step" style="top:232px">Establish the project's information requirements</div>
  <div class="step" style="top:267px">Establish the project's information delivery milestones</div>
  <div class="step" style="top:302px">Establish the project's information standards</div>
  <div class="step" style="top:337px">Establish the project's information production methods and procedures</div>
  <div class="step" style="top:373px">Establish the project's reference information and shared resources</div>
</section>

<!-- Lesson -->
<section class="screen" style="left:844px;top:470px;height:408px">
  <div class="abs" role="img" aria-label="Video of an instructor teaching at a whiteboard" style="left:0;right:0;top:0;height:96px;background:linear-gradient(120deg,#5a4536,#d9d4cf 45%,#ecebe8)"></div>
  <div class="abs" style="left:82px;top:42px;width:11px;height:11px;border-radius:50%;background:#fff;color:var(--pink);font-size:6px;line-height:11px;text-align:center">▶</div>
  <div class="abs" style="left:8px;right:14px;top:110px;height:196px;background:#f8f7f9;box-shadow:0 1px 4px rgba(0,0,0,.07)"></div>
  <div class="abs" style="left:14px;right:20px;top:118px;font-size:7.5px;line-height:1.2;border-left:1.5px solid var(--pink);padding-left:6px;font-weight:500">Appoint Individuals to undertake the information management function.</div>
  <div class="abs" style="left:20px;right:22px;top:145px;font-size:6.8px;line-height:1.35;color:var(--muted)">
    <p>Lorem ipsum dolor sit amet, consetetur sadipscing elitr, sed diam nonumy eirmod tempor invidunt.</p>
    <p style="margin-top:7px">ut labore et dolore magna aliquyam erat, sed diam voluptua. At vero eos et accusam et justo duo dolores et ea rebum. Stet clita kasd gubergren, no sea takimata sanctus.</p>
    <p style="margin-top:7px">Lorem ipsum dolor sit amet, consetetur sadipscing elitr, sed diam nonumy eirmod tempor invidunt ut labore et dolore magna aliquyam erat, sed diam voluptua. At vero eos et accusam et justo duo.</p>
  </div>
  <div class="abs" style="right:22px;top:291px;font-size:6px">Start →</div>
  <div class="abs" style="left:20px;top:322px;font-size:7.5px;font-weight:600">Attachments</div>
  <div class="attach" style="top:337px"><i class="doc"></i>Lorem ipsum dolor sit amet<span class="dl">⤓</span></div>
  <div class="attach" style="top:360px"><i class="doc"></i>Lorem ipsum dolor sit amet<span class="dl">⤓</span></div>
</section>

</body>
</html>
```